Business Card - MosswickTreasury.com

I need a business card that has my photo. It should say: My Pemakino store can be found on at the MosswickTreasury.com. Also find my links to Facebook, Youtube and Tiktok. (If this can be done graphically, then that's even better)

```html
<!DOCTYPE html>
<html lang="en">
<head>
<meta charset="utf-8">
<title>MosswickTreasury Business Card</title>
<link href="https://fonts.googleapis.com/css2?family=Jost:wght@300;400;500&display=swap" rel="stylesheet">
<style>
  :root {
    --bg: #dfe8f8;
    --ink: #111111;
    --black: #0e0e0e;
    --paper: #ffffff;
    --rule: #b9b9b9;
    --silver: #b5b5b5;
    --photo-a: #8a8a8a;
    --photo-b: #5c5c5c;
    --photo-accent: #e0b43a;
  }
  * { box-sizing: border-box; margin: 0; padding: 0; }
  html, body { width: 1200px; height: 900px; overflow: hidden; }
  body {
    background: var(--bg);
    font-family: "Jost", sans-serif;
    color: var(--ink);
    position: relative;
  }
  .card {
    position: absolute;
    width: 540px;
    height: 309px;
    top: 296px;
    box-shadow: 0 6px 18px rgba(0,0,0,.18);
    overflow: hidden;
  }
  /* Front */
  .card-front { left: 40px; background: var(--paper); }
  .front-band {
    position: absolute; left: 0; top: 0;
    width: 130px; height: 222px;
    background: var(--black);
  }
  .portrait-frame {
    position: absolute; left: 58px; top: 18px;
    width: 156px; height: 184px;
    background: var(--paper);
    border: 1px solid var(--rule);
    padding: 6px;
  }
  .portrait {
    width: 100%; height: 100%;
    background: linear-gradient(135deg, var(--photo-a), var(--photo-b) 70%),
                var(--photo-b);
    position: relative;
  }
  .portrait::after {
    content: ""; position: absolute; left: 0; bottom: 0;
    width: 30%; height: 28%;
    background: var(--photo-accent); opacity: .8;
  }
  .brand-block { position: absolute; left: 236px; top: 62px; }
  .brand-name {
    font-size: 31px; font-weight: 400; letter-spacing: .2px; line-height: 1;
  }
  .hours {
    font-size: 9px; font-weight: 400; margin: 5px 0 0 26px;
  }
  .store-line {
    font-size: 14px; font-weight: 400; margin: 22px 0 0 18px;
  }
  .found-line {
    font-size: 19px; font-weight: 500; margin: 0 0 0 -4px; line-height: 1.1;
  }
  .site {
    font-size: 10px; font-weight: 300; letter-spacing: 3px; margin: 2px 0 0 2px;
  }
  .links {
    position: absolute; left: 14px; right: 14px; bottom: 18px;
    height: 30px;
    display: flex; align-items: center;
  }
  .link {
    flex: 1; display: flex; align-items: center; gap: 6px;
    font-size: 9px; font-weight: 400; padding: 0 10px;
  }
  .link + .link { border-left: 1px solid var(--rule); }
  .link-mark {
    width: 11px; height: 11px; background: var(--ink); flex: none;
  }
  /* Back */
  .card-back { left: 620px; background: var(--black); }
  .back-frame {
    position: absolute; inset: 14px;
    border: 1px solid #5a5a5a;
  }
  .back-title {
    position: absolute; left: 0; right: 0; top: 112px;
    text-align: center;
    font-size: 40px; font-weight: 300; color: var(--silver);
  }
  .back-site {
    position: absolute; left: 128px; top: 166px;
    font-size: 10px; font-weight: 300; letter-spacing: 3px; color: var(--silver);
  }
</style>
</head>
<body>
  <section class="card card-front">
    <div class="front-band"></div>
    <div class="portrait-frame">
      <div class="portrait" role="img" aria-label="Portrait photo of the store owner"></div>
    </div>
    <div class="brand-block">
      <h1 class="brand-name">MosswickTreasury</h1>
      <p class="hours">Open 09:00 am – 10:00 pm</p>
      <p class="store-line">My Pemakino store</p>
      <p class="found-line">can be found on at the</p>
      <p class="site">mosswicktreasury.com</p>
    </div>
    <div class="links">
      <div class="link"><span class="link-mark"></span>www.pagenest.com/mosswick</div>
      <div class="link"><span class="link-mark"></span>www.vidhaven.com/c/mosswick</div>
      <div class="link"><span class="link-mark"></span>www.shortloop.com/mosswick</div>
    </div>
  </section>

  <section class="card card-back">
    <div class="back-frame"></div>
    <h2 class="back-title">MosswickTreasury</h2>
    <p class="back-site">mosswicktreasury.com</p>
  </section>
</body>
</html>
```